cartNest - a stylish trolley for apartments

We neede a simple website to sell our Trolley, for apartment use.
The colour theme is red, blask & white. Our logo is attached and this needs to be on the Home page.
The website only needs a Home Page plus 4 other pges.
In the attachment you will find a site map.

You can check out the following two sites to see what I like:
www.plinthgallery.example/design-showcase-inspiration/minimalist-portfolio-website/
www.brightquarry.example/inspiration/40-beautiful-web-design-portfolios/ in this site especially
Dario Menezes
K B Forge
Nine 17 Studio
Oliver Marsh

And especially Lamp - I ike the simpicity of the site esp as we are only selling one product

Target Market(s)

Apartment dwellers

Industry/Entity Type

Apartment

Requirements
Must have
• This website must have 4 pages.
We need Corvo, Ledgerline and Quidly portals.
Order Form for Trolley
Payment form.

```html
<!DOCTYPE html>
<html lang="en">
<head>
<meta charset="utf-8">
<title>cartNest – a stylish trolley for apartments</title>
<link rel="stylesheet" href="https://fonts.googleapis.com/css2?family=Arimo:wght@400;700&family=Playfair+Display:ital,wght@0,400;1,700&display=swap">
<style>
:root{
  --red:#8e0b0b;
  --red-bright:#c4121a;
  --ink:#111;
  --grey-text:#7a7a7a;
  --header:#1e1e1e;
  --band:#ececec;
  --panel:#dcdcdc;
  --white:#fff;
  --footer-bar:#0c0c0c;
  --gold:#e8b21a;
}
*{margin:0;padding:0;box-sizing:border-box}
html,body{width:1037px;height:1200px;overflow:hidden}
body{position:relative;font-family:Arimo,Arial,sans-serif;background:#f1f1f1;color:var(--ink)}
.abs{position:absolute}

.site-header{left:0;top:0;width:1037px;height:140px;background:linear-gradient(#2a2a2a,#141414)}
.brand{left:33px;top:40px;display:flex;align-items:center;gap:10px}
.brand-mark{width:30px;height:30px;background:var(--red-bright)}
.brand-name{font-size:30px;font-weight:700;color:var(--white)}
.hotline{left:768px;top:18px;display:flex;align-items:center;gap:10px}
.hotline-number{font-size:29px;font-weight:700;color:#d8d8d8}

.hero-panel{left:588px;top:77px;width:445px;height:534px;background:var(--panel);box-shadow:0 0 10px rgba(0,0,0,.35)}
.main-nav{left:603px;top:83px;display:flex;height:68px;align-items:center}
.main-nav a{display:block;font-size:16px;font-weight:700;color:var(--red);text-decoration:none;padding:0 15px;line-height:68px}
.main-nav a.is-active{background:var(--red);color:var(--white);width:85px;text-align:center;padding:0;margin-right:1px;border:1px solid #b01a1a}
.hero-visual{left:603px;top:156px;width:413px;height:440px;background:linear-gradient(135deg,#b8b8b5 0%,#8a847c 55%,#6b3a2a 100%)}
.hero-caption{left:603px;top:449px;width:413px;height:147px;background:rgba(225,210,195,.78);border:2px solid #b2733d;text-align:center;font-family:"Playfair Display",serif;color:#2a0505}
.hero-caption .line1{font-size:42px;margin-top:22px;line-height:1}
.hero-caption .line1 em{font-style:italic;font-weight:700}
.hero-caption .line2{font-size:52px;line-height:1.05}

.intro{left:3px;top:180px;width:557px}
.intro h2{font-size:19px;font-weight:400;text-decoration:underline;margin-bottom:12px}
.intro h2 span{color:var(--red-bright);font-weight:700;font-size:21px;margin-left:8px}
.intro p{font-size:11.5px;line-height:19.5px;color:var(--grey-text)}
.intro p b{color:var(--ink);font-size:16px}
.intro p a{color:var(--ink);font-size:11.5px}
.intro .uses{margin-top:18px}
.btn-more{left:3px;top:574px;width:84px;height:28px;border-radius:5px;background:linear-gradient(#555,#111);color:var(--white);font-size:12px;font-weight:700;line-height:28px;text-align:center}

.gallery-band{left:0;top:613px;width:1037px;height:327px;background:var(--band)}
.gallery-label{left:11px;top:659px;width:109px;height:38px;border:2px solid #fff;border-radius:3px;background:linear-gradient(#e2e2e2,#c4c4c4);box-shadow:0 0 3px rgba(0,0,0,.4);font-size:19px;font-weight:700;color:#6b6b6b;text-align:center;line-height:34px}
.pager{left:957px;top:676px;display:flex;gap:5px}
.pager i{display:block;width:8px;height:10px;background:#999}
.pager i.is-active{background:var(--red)}
.thumb{top:717px;height:174px}
.thumb-1{left:5px;width:202px;background:linear-gradient(#7b7457,#4a4f3d)}
.thumb-2{left:212px;width:201px;background:linear-gradient(#6f6e5a,#b9b9a8)}
.thumb-3{left:417px;width:202px;background:linear-gradient(#a09c8f,#5d5a53)}
.thumb-4{left:624px;width:201px;background:linear-gradient(#c8cdd2,#9aa4ac)}
.thumb-5{left:831px;width:200px;background:linear-gradient(#3a2a22,#b9b5ad)}
.slider-arrow{top:767px;width:43px;height:66px;background:rgba(235,235,235,.9);font-size:26px;color:#333;text-align:center;line-height:66px}
.shadow-bar{left:110px;top:896px;width:820px;height:14px;border-radius:50%;background:radial-gradient(rgba(0,0,0,.25),transparent 70%)}

.site-footer{left:0;top:940px;width:1037px;height:223px;background:var(--white)}
.col{top:956px;font-size:13px;line-height:19px;color:#222}
.col h3{font-size:13px;font-weight:700;margin-bottom:14px}
.testimonials{left:3px;width:340px}
.testimonials .author{text-align:right;padding-right:16px;margin-bottom:8px}
.payment{left:413px;width:310px}
.pay-cards{display:flex;gap:8px;margin-bottom:20px}
.pay-cards span{display:block;padding:0 4px;height:22px;border:1px solid #aaa;font-size:10px;line-height:20px;color:#234}
.pay-row{display:flex;gap:10px;align-items:flex-start;margin-bottom:16px}
.pay-row a{color:#222}
.contact{left:751px;width:285px}
.contact-row{display:flex;gap:14px;align-items:flex-start;margin-bottom:26px}
.contact-row a{color:var(--red-bright)}
.contact-row .phone{font-size:19px;font-weight:700;margin-top:6px}
.copyright{left:0;top:1163px;width:1037px;height:37px;background:var(--footer-bar);color:#bbb;font-size:12px;text-align:center;line-height:37px}
</style>
</head>
<body>

<header class="site-header abs"></header>
<div class="brand abs"><span class="brand-mark"></span><span class="brand-name">cartNest</span></div>
<div class="hotline abs">
  <svg width="54" height="54" viewBox="0 0 54 54" aria-hidden="true"><circle cx="27" cy="27" r="26" fill="var(--gold)"/><path d="M18 17c3-2 5 0 6 3l-2 3c1 3 4 6 7 7l3-2c3 1 5 3 3 6-2 3-6 3-10 0s-9-8-9-12c0-2 1-4 2-5z" fill="#2a2a2a"/></svg>
  <span class="hotline-number">+014 27730981</span>
</div>

<div class="hero-panel abs"></div>
<nav class="main-nav abs">
  <a class="is-active" href="#">HOME</a>
  <a href="#">ABOUT US</a>
  <a href="#">CONTACT US</a>
  <a href="#">NEWS</a>
</nav>
<div class="hero-visual abs" role="img" aria-label="Chrome apartment trolley loaded with red suitcases and shopping bags in a hallway"></div>
<div class="hero-caption abs">
  <div class="line1"><em>a stylish</em> TROLLEY</div>
  <div class="line2">for apartments</div>
</div>

<section class="intro abs">
  <h2>WELCOME TO <span>cartNest</span></h2>
  <p><b>cartNest</b> evolved from demand!&nbsp; Apartment dwellers everywhere are calling for a solution to moving shopping, luggage and other goods from car to apartment, and vice versa. Other trolleys on the market are not versatile, they are not robust, but more importantly, they are NOT stylish! The emphasis of cartNest is on style. This trolley is stylish enough to remain in your apartment as a piece of furniture. It features a versatile flat-bed and hanger, to cope with all your transport needs.cartNest evolved from demand!&nbsp; Apartment dwellers everywhere are calling for a solution to moving shopping, luggage and other goods from car to apartment, and vice versa. Other trolleys on the market are not versatile, they are not robust, but more importantly, they are NOT stylish! The emphasis of cartNest is on style. This trolley is stylish enough to remain in your apartment as a piece of furniture. It features a versatile flat-bed and hanger, to cope with all your transport needs.<a href="#">MORE</a></p>
  <h2 class="uses">USES </h2>
  <p><b>cartNest</b> evolved from demand!&nbsp; Apartment dwellers everywhere are calling for a solution to moving shopping, luggage and other goods from car to apartment, and vice versa. Other trolleys on the market are not versatile, they are not robust, but more importantly, they are NOT stylish! The emphasis of cartNest is on style. This trolley is stylish enough to remain in your apartment a <a href="#">.MORE</a></p>
</section>
<div class="btn-more abs">Read More</div>

<section class="gallery-band abs"></section>
<div class="gallery-label abs">Gallery</div>
<div class="pager abs"><i class="is-active"></i><i></i><i></i><i></i><i></i></div>
<div class="thumb thumb-1 abs" role="img" aria-label="Man hanging a garment bag on the trolley"></div>
<div class="thumb thumb-2 abs" role="img" aria-label="Unloading a car boot onto the trolley in a car park"></div>
<div class="thumb thumb-3 abs" role="img" aria-label="Loaded trolley in a lift lobby"></div>
<div class="thumb thumb-4 abs" role="img" aria-label="Close-up of the chrome hanger rail"></div>
<div class="thumb thumb-5 abs" role="img" aria-label="Close-up of the trolley wheels"></div>
<div class="slider-arrow abs" style="left:5px">&#10095;</div>
<div class="slider-arrow abs" style="left:988px">&#10094;</div>
<div class="shadow-bar abs"></div>

<footer class="site-footer abs"></footer>
<div class="col testimonials abs">
  <h3>Testimonial</h3>
  <p>Lorem Ipsum is simply dummy text of the printing and typesetting industry&nbsp; Lorem Ipsum is simply dummy text of the printing and typesetting</p>
  <p class="author">- Renata Hale</p>
  <p>Lorem Ipsum is simply dummy text of the printing and typesetting industry&nbsp; Lorem Ipsum is simply dummy text of the printing and typesetting</p>
  <p class="author">- Renata Hale</p>
</div>
<div class="col payment abs">
  <h3>Payment Option</h3>
  <div class="pay-cards"><span>Quidly</span><span>Corvo</span><span>Ledgerline</span></div>
  <div class="pay-row">
    <svg width="30" height="34" viewBox="0 0 30 34" aria-hidden="true"><rect x="2" y="2" width="24" height="30" fill="#e8eef4" stroke="#7890a8"/><path d="M7 10h14M7 16h14M7 22h10" stroke="#7890a8" stroke-width="2"/></svg>
    <p>Like “cartNest” ORDER NOW<br><a href="#">Click here to fill order form</a></p>
  </div>
  <div class="pay-row">
    <svg width="30" height="34" viewBox="0 0 30 34" aria-hidden="true"><rect x="2" y="2" width="24" height="30" fill="#fdf3dc" stroke="#c08a2a"/><path d="M7 10h14M7 16h14M7 22h10" stroke="#c08a2a" stroke-width="2"/></svg>
    <p>Make your Payment to easy way - <a href="#">payment FORM</a></p>
  </div>
</div>
<div class="col contact abs">
  <div class="contact-row">
    <svg width="30" height="34" viewBox="0 0 30 34" aria-hidden="true"><rect x="3" y="2" width="24" height="30" rx="3" fill="#3a7cc4"/><circle cx="15" cy="17" r="6" fill="none" stroke="#fff" stroke-width="2"/></svg>
    <p>Suite 212, 4470 Halden Row NW, Mercer Square, Ashford</p>
  </div>
  <div class="contact-row">
    <svg width="32" height="26" viewBox="0 0 32 26" aria-hidden="true"><rect x="1" y="3" width="30" height="20" fill="#dfe8f2" stroke="#6c8aa8"/><path d="M1 3l15 11 15-11" fill="none" stroke="#6c8aa8" stroke-width="2"/></svg>
    <p><a href="#">hello@cartnest.example</a></p>
  </div>
  <div class="contact-row">
    <svg width="34" height="34" viewBox="0 0 34 34" aria-hidden="true"><rect x="1" y="1" width="32" height="32" rx="6" fill="#4caa3c"/><path d="M11 9c2-1 4 0 4 2l-1 3c1 2 3 4 5 5l2-1c2 0 3 2 2 4-2 2-5 1-8-1s-6-6-6-9c0-1 1-2 2-3z" fill="#fff"/></svg>
    <p class="phone">+014 6620357718</p>
  </div>
</div>
<div class="copyright abs">Copyright © 2011 cartnest.example</div>

</body>
</html>
```